Financial Book Cover Design (Subject: exponential technologies)

We are in need of a FRONT, BACK and SPINE design for an upcoming book titled: Quiet Harbor Plans: An Almanac For Every Season, Tide and Distant Shore.

REQUIREMENTS:
TITLE:Quiet Harbor Plans: An Almanac For Every Season, Tide and Distant Shore

PHOTOS: as designer sees fit, author must be on someplace.

SIZE OF BOOK:
Cove - 7.25 inches wide, 9.25 inches tall
Spine - 1.25 inches

ABOUT THE BOOK:
Advances in exponential technologies will affect virtually every aspect of life on our planet. Innovation will touch everything we do, from how we communicate to the way we manage our personal finances. They will affect how you’ll learn, work, live and love.

Advances in networks and computer systems, robotics, big data, nanotechnology, medicine and neuroscience, biotechnology, energy and environmental systems, materials science, and financial services technology are quickly changing everything. Due to such innovations as tennis rackets that track the speed of your forehand, backhand, serve or smash ($200, available now) to the world’s largest indoor, vertical farm that produces two million pounds of produce annually without soil or sunlight (Newark, New Jersey), your life will never be the same.

These shocking innovations will alter every aspect of your personal finances, from how long you’ll live (most likely, well into your 100s), when you’ll retire (you won’t, at least not for many decades), to where you work (not where you work now), what you do (you’ll engage in a new occupation, maybe several), how to save for college (you won’t have to) and pay for long-term care (ditto), choosing where to live (in communities built just for you), how you’ll save (adapting investment strategies that have never before existed) and how many spouses you’ll have and where you’ll find them (!).

Because of all the changes that are coming, it’s vital that you alter your strategies for handling your personal finances. If you manage your money the way prior generations managed theirs, you will fail where they succeeded.

• REQUIREMENTS:
• TITLE:Quiet Harbor Plans: An Almanac For Every Season, Tide and Distant Shore
• PHOTOS: as designer sees fit, author must be on someplace.
• SIZE OF BOOK:
• Cove - 7.25 inches wide, 9.25 inches tall
• Spine - 1.25 inches

```html
<!DOCTYPE html>
<html lang="en">
<head>
<meta charset="utf-8">
<title>Quiet Harbor Plans – Book Cover</title>
<link rel="stylesheet" href="https://fonts.googleapis.com/css2?family=Roboto+Condensed:ital,wght@0,300;0,700;1,300&family=Roboto:ital,wght@0,700;1,900&family=Montserrat:wght@400&display=swap">
<style>
  :root {
    --sky-deep: #0b4fc4;
    --sky-mid: #1f74e0;
    --sky-light: #5aa6f0;
    --cloud: #e8f2fc;
    --suit: #15171c;
    --ink: #0a0a0a;
    --white: #ffffff;
  }
  * { margin: 0; padding: 0; box-sizing: border-box; }
  html, body { width: 1200px; height: 705px; overflow: hidden; background: var(--white); }
  .cover {
    position: relative;
    width: 1200px;
    height: 705px;
    overflow: hidden;
    color: var(--white);
  }
  .sky-photo {
    position: absolute; inset: 0;
    background:
      radial-gradient(ellipse 420px 140px at 300px 660px, rgba(232,242,252,0.85), rgba(232,242,252,0) 70%),
      radial-gradient(ellipse 160px 340px at 700px 330px, rgba(232,242,252,0.55), rgba(232,242,252,0) 70%),
      linear-gradient(180deg, var(--sky-deep) 0%, var(--sky-mid) 55%, var(--sky-light) 100%);
  }
  .author-photo {
    position: absolute;
    left: 935px; top: 30px; width: 265px; height: 675px;
    border-radius: 120px 0 0 0;
    background: linear-gradient(180deg, rgba(21,23,28,0.15) 0%, rgba(21,23,28,0.75) 30%, var(--suit) 100%);
  }

  /* Back cover */
  .back { position: absolute; left: 0; top: 0; width: 576px; height: 705px; }
  .back-title { position: absolute; left: 56px; top: 34px; line-height: 1; }
  .back-title .lead {
    display: block;
    font: 300 36px/1 "Roboto Condensed", sans-serif;
  }
  .back-title .main {
    display: block;
    font: 700 53px/0.92 "Roboto", sans-serif;
    letter-spacing: 0.5px;
  }
  .back-subtitle {
    position: absolute; left: 59px; top: 169px;
    font: 300 12px/1 "Roboto Condensed", sans-serif;
    text-transform: uppercase;
  }
  .blurb {
    position: absolute; left: 40px; top: 211px; width: 490px;
    font: 400 11.2px/14px "Montserrat", sans-serif;
    text-align: center;
  }
  .blurb p + p { margin-top: 14px; }

  /* Spine */
  .spine {
    position: absolute; left: 576px; top: 0; width: 48px; height: 705px;
  }
  .spine-title {
    position: absolute; left: 4px; top: 26px;
    writing-mode: vertical-rl;
    font: 700 40px/40px "Roboto Condensed", sans-serif;
    text-transform: uppercase;
    white-space: nowrap;
    color: var(--ink);
  }
  .spine-author {
    position: absolute; left: 6px; bottom: 22px;
    writing-mode: vertical-rl;
    font: 700 36px/36px "Roboto Condensed", sans-serif;
    letter-spacing: -0.5px;
    text-transform: uppercase;
    white-space: nowrap;
    color: var(--white);
  }

  /* Front cover */
  .front { position: absolute; left: 624px; top: 0; width: 576px; height: 705px; }
  .front-author {
    position: absolute; left: 76px; top: 46px;
    font: 700 32px/1 "Roboto", sans-serif;
    letter-spacing: 0.3px;
  }
  .front-title { position: absolute; left: 52px; top: 408px; }
  .front-title .lead {
    display: block;
    font: italic 300 74px/1 "Roboto Condensed", sans-serif;
    margin-left: 12px;
  }
  .front-title .main {
    display: block;
    font: italic 900 92px/0.96 "Roboto", sans-serif;
    letter-spacing: -1px;
  }
  .front-subtitle {
    position: absolute; left: 52px; top: 656px;
    font: 300 20px/1 "Roboto Condensed", sans-serif;
    text-transform: uppercase;
  }
</style>
</head>
<body>
<main class="cover">
  <div class="sky-photo" role="img" aria-label="Bright blue sky with a white cloud shaped like a rising arrow sweeping from lower left up across the spine"></div>
  <div class="author-photo" role="img" aria-label="Portrait of the smiling author in a dark suit and light blue shirt, arms open in a welcoming gesture"></div>

  <section class="back">
    <h2 class="back-title">
      <span class="lead">QUIET</span>
      <span class="main">HARBOR</span>
      <span class="main">PLANS</span>
    </h2>
    <p class="back-subtitle">An Almanac For Every Season, Tide and Distant Shore</p>
    <div class="blurb">
      <p>Advances in exponential technologies will affect virtually every aspect of life on our planet. Innovation will touch everything we do, from how we communicate to the way we manage our personal finances. They will affect how you’ll learn, work, live and love.</p>
      <p>Advances in networks and computer systems, robotics, big data, nanotechnology, medicine and neuroscience, biotechnology, energy and environmental systems, materials science, and financial services technology are quickly changing everything. Due to such innovations as tennis rackets that track the speed of your forehand, backhand, serve or smash ($200, available now) to the world’s largest indoor, vertical farm that produces two million pounds of produce annually without soil or sunlight (Newark, New Jersey), your life will never be the same.</p>
      <p>These shocking innovations will alter every aspect of your personal finances, from how long you’ll live (most likely, well into your 100s), when you’ll retire (you won’t, at least not for many decades), to where you work (not where you work now), what you do (you’ll engage in a new occupation, maybe several), how to save for college (you won’t have to) and pay for long-term care (ditto), choosing where to live (in communities built just for you), how you’ll save (adapting investment strategies that have never before existed) and how many spouses you’ll have and where you’ll find them (!).</p>
      <p>Because of all the changes that are coming, it’s vital that you alter your strategies for handling your personal finances. If you manage your money the way prior generations managed theirs, you will fail where they succeeded.</p>
    </div>
  </section>

  <section class="spine">
    <span class="spine-title">QUIET HARBOR PLANS</span>
    <span class="spine-author">AUTHOR NAME</span>
  </section>

  <section class="front">
    <p class="front-author">AUTHOR NAME</p>
    <h1 class="front-title">
      <span class="lead">QUIET</span>
      <span class="main">HARBOR</span>
      <span class="main">PLANS</span>
    </h1>
    <p class="front-subtitle">An Almanac For Every Season, Tide and Distant Shore</p>
  </section>
</main>
</body>
</html>
```